Pamphlet for IT Services Company (MSP Provider or Managed Services Provider)

We need a pamphlet designed for our Managed Services Company. We are an established company of 17 years that has never advertised. We'd like a pamphlet that we can drop off at potential client sites that describes our services. I like clean and prefer Orange as an accent color. We'd like to touch on the fact that we cater to our clients needs and go above and beyond what the other providers do.

Target Market(s)

Small and Medium Sized Businesses

Industry/Entity Type

It Service

Font styles to use
Other font styles liked:
• Try to match font on logo or website

Requirements
Must have
• Must highlight with the following Services and descriptions with Logo
Managed IT Services
IT Support
VOIP Solutions
WiFI Solutions
Contact information with phone number and website address.
Please view website korvantech.com
try to match fons on website above.
Nice to have
• Customer Testimonials. May a couple one line testimonials. Not real sure because this is the first time we've ever designed a brochure.
Should not have
• Not Sure

```html
<!DOCTYPE html>
<html lang="en">
<head>
<meta charset="utf-8">
<title>Korvan Technologies – Managed IT Services</title>
<link rel="stylesheet" href="https://fonts.googleapis.com/css2?family=Lato:ital,wght@0,300;0,400;0,700;0,900;1,700&display=swap">
<style>
  :root {
    --orange: #f58a2e;
    --navy: #222a36;
    --cream: #fdf6ec;
    --white: #ffffff;
    --stage: #9a9a9a;
    --ink: #1f2530;
    --badge: #8e8e8e;
  }
  * { box-sizing: border-box; margin: 0; padding: 0; }
  html, body { width: 1001px; height: 1200px; overflow: hidden; }
  body { background: var(--stage); font-family: 'Lato', sans-serif; color: var(--ink); position: relative; }

  .pamphlet { position: absolute; left: 74px; top: 48px; width: 854px; height: 1104px; background: var(--white); overflow: hidden; }

  .masthead { height: 124px; display: flex; align-items: center; justify-content: center; padding-top: 8px; }
  .brand-name { font-size: 36px; font-weight: 400; color: var(--orange); letter-spacing: 0.2px; }

  .hero { position: absolute; left: 0; top: 124px; width: 854px; height: 556px;
    background:
      radial-gradient(ellipse at 15% 25%, rgba(236,150,120,.55), transparent 45%),
      radial-gradient(ellipse at 80% 55%, rgba(200,190,200,.45), transparent 40%),
      radial-gradient(ellipse at 90% 10%, rgba(230,170,110,.5), transparent 35%),
      linear-gradient(160deg, #6d3b5e 0%, #4a3c6e 45%, #2f3556 100%); }
  .hero-copy { position: absolute; top: 92px; left: 0; width: 100%; text-align: center; color: var(--white); }
  .hero-title { font-size: 47px; font-weight: 900; line-height: 1; letter-spacing: 0.3px; }
  .hero-sub { font-size: 26px; font-weight: 700; margin-top: 18px; }
  .hero-rule { width: 48px; height: 2px; background: var(--orange); margin: 22px auto 0; }
  .hero-text { font-size: 15.5px; font-weight: 700; line-height: 24px; margin: 20px auto 0; width: 630px; }

  .service { position: absolute; top: 503px; width: 251px; height: 373px; text-align: center; padding: 0 34px; box-shadow: 0 3px 8px rgba(0,0,0,.18); }
  .service-icon { display: block; margin: 22px auto 0; height: 62px; }
  .service-title { font-size: 24px; font-weight: 400; margin-top: 18px; }
  .service-body { font-size: 13.2px; line-height: 17.5px; margin-top: 24px; }
  .service-body p + p { margin-top: 17px; }
  .service-body em { font-weight: 700; font-style: italic; }
  .service--support { left: 35px; background: var(--cream); color: var(--ink); }
  .service--voip { left: 301px; width: 250px; background: var(--orange); color: var(--white); }
  .service--wifi { left: 566px; background: var(--navy); color: var(--white); }

  .partners { position: absolute; top: 922px; left: 60px; width: 726px; display: flex; align-items: center; justify-content: space-between; }
  .partner-badge { background: var(--badge); opacity: .55; }

  .footer-rule { position: absolute; left: 0; top: 1006px; width: 100%; height: 5px; background: var(--orange); }
  .footer { position: absolute; left: 0; top: 1011px; width: 100%; height: 93px; background: var(--navy); color: var(--white); }
  .call { position: absolute; left: 52px; top: 18px; display: flex; gap: 12px; }
  .call-label { font-size: 17px; font-weight: 700; letter-spacing: .4px; }
  .call-number { font-size: 25px; font-weight: 700; margin-top: 2px; }
  .divider { position: absolute; left: 420px; top: 16px; height: 62px; border-left: 2px dotted #6d7585; }
  .contact { position: absolute; left: 468px; top: 24px; font-size: 15px; line-height: 23px; font-weight: 400; }
  .contact b { font-weight: 700; }
  .social { position: absolute; left: 738px; top: 50px; display: flex; gap: 6px; }
  .social span { width: 17px; height: 17px; border-radius: 50%; background: var(--white); }
</style>
</head>
<body>
<main class="pamphlet">
  <header class="masthead">
    <span class="brand-name">korvan technologies</span>
  </header>

  <section class="hero" role="img" aria-label="Photo of a hand touching a tablet with soft blurred city lights">
    <div class="hero-copy">
      <h1 class="hero-title">Managed IT Services</h1>
      <p class="hero-sub">Let us take care of your IT</p>
      <div class="hero-rule"></div>
      <p class="hero-text">Our MSP is a Flat Rate service that includes Onsite &amp; Remote Support, Endpoint Protection, Web Filtering, Encrypted Online Backup &amp; Patch Management</p>
    </div>
  </section>

  <article class="service service--support">
    <svg class="service-icon" width="66" height="62" viewBox="0 0 66 62" aria-hidden="true">
      <rect x="3" y="3" width="60" height="42" rx="4" fill="none" stroke="#1f2530" stroke-width="3.5"/>
      <path d="M33 45 V54 M20 57 H46" stroke="#1f2530" stroke-width="3.5" stroke-linecap="round"/>
      <path d="M24 33 H42 a6 6 0 0 0 0-12 a8 8 0 0 0-15-2 a6 6 0 0 0-3 14 Z" fill="none" stroke="#1f2530" stroke-width="3"/>
    </svg>
    <h2 class="service-title">IT Support</h2>
    <div class="service-body">
      <p><em>We have a passion for what we do and it shows!</em></p>
      <p>Korvan provides fast, reliable, expert solutions from experienced staff. You will never feel like just another client to us because our customers are family!</p>
    </div>
  </article>

  <article class="service service--voip">
    <svg class="service-icon" width="62" height="62" viewBox="0 0 62 62" aria-hidden="true">
      <path d="M12 8 l8-3 l7 12 l-5 5 c3 7 8 12 15 15 l5-5 l12 7 l-3 8 c-2 5-9 6-15 3 C25 45 17 37 12 26 C9 20 8 12 12 8 Z" fill="none" stroke="#fff" stroke-width="3" stroke-linejoin="round"/>
      <path d="M35 8 a20 20 0 0 1 19 19 M35 16 a12 12 0 0 1 11 11 M35 23 a4 4 0 0 1 4 4" fill="none" stroke="#fff" stroke-width="3" stroke-linecap="round"/>
    </svg>
    <h2 class="service-title">VOIP Solutions</h2>
    <div class="service-body">
      <p>Phones are more than just an attachment to a desk. <em>Allow us to help you maximize communication</em> with your team and customers by using the latest technology that will likely save you money as well. Korvan Technologies partners with Linecrest to provide phone hardware, systems, and phone service.</p>
    </div>
  </article>

  <article class="service service--wifi">
    <svg class="service-icon" width="66" height="62" viewBox="0 0 66 62" aria-hidden="true">
      <path d="M5 22 a40 40 0 0 1 56 0 M14 32 a27 27 0 0 1 38 0 M23 42 a14 14 0 0 1 20 0" fill="none" stroke="#fff" stroke-width="5" stroke-linecap="round"/>
      <circle cx="33" cy="53" r="5" fill="#fff"/>
    </svg>
    <h2 class="service-title">WiFi Solutions</h2>
    <div class="service-body">
      <p>WiFi is everywhere!<br>(At least it should be.)</p>
      <p>Korvan can <em>extend your WiFi</em> to cover your whole campus.</p>
    </div>
  </article>

  <section class="partners" aria-label="Technology partners">
    <div class="partner-badge" style="width:78px;height:48px;border-radius:4px"></div>
    <div class="partner-badge" style="width:50px;height:48px;border-radius:4px"></div>
    <div class="partner-badge" style="width:126px;height:30px;border-radius:4px"></div>
    <div class="partner-badge" style="width:112px;height:20px;border-radius:4px"></div>
    <div class="partner-badge" style="width:96px;height:30px;border-radius:4px"></div>
    <div class="partner-badge" style="width:126px;height:38px;border-radius:2px;opacity:.8;background:#4a4a4a"></div>
  </section>

  <div class="footer-rule"></div>
  <footer class="footer">
    <div class="call">
      <svg width="24" height="24" viewBox="0 0 24 24" aria-hidden="true">
        <path d="M5 3 l3-1 l3 5 l-2 2 c1 3 3 5 6 6 l2-2 l5 3 l-1 3 c-1 2-4 2-6 1 C10 18 6 14 4 9 C3 7 3 4 5 3 Z" fill="none" stroke="#fff" stroke-width="1.6" stroke-linejoin="round"/>
        <path d="M14 3 a7 7 0 0 1 7 7 M14 7 a3 3 0 0 1 3 3" fill="none" stroke="#fff" stroke-width="1.6" stroke-linecap="round"/>
      </svg>
      <div>
        <p class="call-label">CALL US:</p>
        <p class="call-number">+1 (555) 014-2087</p>
      </div>
    </div>
    <div class="divider"></div>
    <div class="contact">
      <p>Website: <b>www.korvantech.com</b></p>
      <p>Email: <b>rhale@korvantech.com</b></p>
    </div>
    <div class="social" aria-hidden="true"><span></span><span></span><span></span></div>
  </footer>
</main>
</body>
</html>
```